Electrician's Business needs web site for customers to get professional impression of business.

Have a logo, need a web page for customers to visit. Web page should make it easy for customers to approach /contact me, if possible a way for customers to leave their details so I can call them back.
A description/ list of services and advertise how my service is different and better than other electricians.
A gallery to upload photos to, to show completed works from past projects.

Target Market(s)

Domestic/residential home owner/renter/builder

Industry/Entity Type

Electrician

Coding

Coded - Design and coding required

Number of Pages Required

2 page

Font styles to use
Sans Serif

Colors
0255a3
ffffff

Requirements
Must have
• Appeal to home owner/renter, domestic market.
• Capture contact details of customer & advertise my contact details.
• List of services
Nice to have
• A photo gallery, so I can upload pictures of completed work.
Should not have
• Industrial/construction images.

```html
<!DOCTYPE html>
<html lang="en">
<head>
<meta charset="utf-8">
<title>Brightwire Electrical Services</title>
<link href="https://fonts.googleapis.com/css2?family=Roboto:wght@400;500;700&family=Roboto+Condensed:wght@400;700&family=Open+Sans:wght@400;600&family=Archivo+Black&display=swap" rel="stylesheet">
<style>
  :root{
    --brand-blue:#0255a3;
    --hero-deep:#3f68cc;
    --hero-light:#7f9fde;
    --panel-start:#1a6fb8;
    --panel-end:#52bdf5;
    --white:#ffffff;
    --ink:#1b2a44;
    --accent:#f7c52a;
    --card-green:#4d6a3a;
    --card-wood:#8a5a32;
    --card-blue:#1f5fc4;
    --card-grey:#b8c2cc;
  }
  *{margin:0;padding:0;box-sizing:border-box}
  html,body{width:1200px;height:676px;overflow:hidden;background:var(--white)}
  body{font-family:'Roboto',sans-serif;position:relative}

  .hero{
    position:absolute;left:0;top:0;width:1200px;height:548px;
    background:linear-gradient(115deg,var(--hero-deep) 0%,var(--hero-deep) 48%,#5b80d6 48%,var(--hero-light) 100%);
  }
  .site-header{
    position:absolute;left:0;top:0;width:1200px;height:76px;
    border-bottom:1px solid rgba(255,255,255,.35);
    display:flex;align-items:center;padding:0 58px 0 46px;
  }
  .brand{display:flex;align-items:center;gap:10px;color:var(--white);font-family:'Roboto',sans-serif;font-weight:700;font-size:26px;letter-spacing:.5px}
  .brand-dot{width:12px;height:12px;border-radius:50%;background:var(--accent)}
  .main-nav{margin-left:auto;display:flex;align-items:center;gap:34px}
  .main-nav a{color:var(--white);text-decoration:none;font-family:'Roboto Condensed',sans-serif;font-size:15px;letter-spacing:.3px}
  .main-nav .nav-cta{border:2px solid var(--white);border-radius:20px;padding:8px 14px;font-weight:700}

  .hero-copy{position:absolute;left:62px;top:190px;width:440px;text-align:center;color:var(--white)}
  .hero-kicker{display:flex;align-items:center;justify-content:center;gap:14px;font-family:'Roboto Condensed',sans-serif;font-size:26px;letter-spacing:.2px}
  .hero-kicker .rule{width:40px;height:8px;background:repeating-linear-gradient(135deg,rgba(255,255,255,.85) 0 2px,transparent 2px 5px)}
  .hero-title{font-family:'Archivo Black',sans-serif;font-size:66px;line-height:1.05;letter-spacing:.5px;text-shadow:0 3px 4px rgba(0,0,0,.3)}
  .hero-phone{font-family:'Open Sans',sans-serif;font-size:21px;margin-top:4px}

  .hero-art{position:absolute;left:790px;top:125px;width:250px;height:280px;border-radius:50%;
    background:radial-gradient(circle,rgba(247,197,42,.35) 0%,rgba(247,197,42,.08) 55%,transparent 72%)}

  .welcome{
    position:absolute;left:70px;top:452px;width:1060px;height:136px;border-radius:3px;
    background:linear-gradient(90deg,var(--panel-start),var(--panel-end));
    color:var(--white);text-align:center;padding:20px 28px;
    box-shadow:0 4px 10px rgba(0,0,0,.15);
  }
  .welcome h2{font-family:'Roboto',sans-serif;font-weight:500;font-size:17px;margin-bottom:16px}
  .welcome p{font-family:'Roboto Condensed',sans-serif;font-size:13px;line-height:1.45}

  .services{position:absolute;left:0;top:600px;width:1200px;text-align:center}
  .services h2{font-family:'Roboto',sans-serif;font-weight:500;font-size:21px;color:var(--ink)}
  .services h2 span{color:var(--brand-blue)}
  .services .divider{width:1070px;margin:12px auto 0;border-top:2px dotted var(--brand-blue)}
  .service-cards{position:absolute;left:70px;top:68px;width:1060px;display:flex;gap:24px}
  .service-card{position:relative;flex:1;height:60px;margin-top:12px}
  .service-card .icon{position:absolute;left:50%;top:-18px;transform:translateX(-50%);width:42px;height:42px;border-radius:50%;background:var(--card-blue);border:2px solid var(--white)}
  .card-1{background:linear-gradient(90deg,var(--card-wood),var(--card-green))}
  .card-2{background:linear-gradient(90deg,#6a7f8f,var(--card-green))}
  .card-3{background:var(--card-blue)}
  .card-4{background:linear-gradient(90deg,var(--card-grey),#d9c7a8)}
</style>
</head>
<body>
  <section class="hero">
    <header class="site-header">
      <div class="brand"><span>Brightwire</span><span class="brand-dot"></span></div>
      <nav class="main-nav">
        <a href="#">HOME</a>
        <a href="#">ABOUT</a>
        <a href="#">SERVICES</a>
        <a href="#">OUR WORK</a>
        <a href="#">BLOG</a>
        <a href="#" class="nav-cta">CONTACT US</a>
      </nav>
    </header>

    <div class="hero-copy">
      <div class="hero-kicker"><span class="rule"></span>DO YOU NEED A NEW<span class="rule"></span></div>
      <h1 class="hero-title">ELECTRICIAN?</h1>
      <p class="hero-phone">Call Brightwire at (555) 014 2368</p>
    </div>

    <div class="hero-art" role="img" aria-label="Yellow line illustration of a glowing light bulb"></div>
  </section>

  <section class="welcome">
    <h2>Welcome We're Brightwire</h2>
    <p>Brightwire Electric's mission is to provide residential and commercial electrical service above and beyond what is expected. We treat each and every customer as if they were a part of the family. In doing so, Brightwire Electric places an emphasis on communicating at every step of the service process. From initial service call, to project completion, we want our customers to know their job is always a priority. Honesty, integrity, and courteous service is what we promise you.</p>
  </section>

  <section class="services">
    <h2>Our <span>Services</span></h2>
    <div class="divider"></div>
    <div class="service-cards">
      <div class="service-card card-1" role="img" aria-label="Photo of a lit home exterior at dusk"><span class="icon"></span></div>
      <div class="service-card card-2" role="img" aria-label="Photo of a house with a backup generator"><span class="icon"></span></div>
      <div class="service-card card-3" role="img" aria-label="Lighting service tile"><span class="icon"></span></div>
      <div class="service-card card-4" role="img" aria-label="Photo of an indoor electrical panel installation"><span class="icon"></span></div>
    </div>
  </section>
</body>
</html>
```